Webdesign for a Bikeshop in Innsbruck (submitted designs will be used for Masterthesis anonymously)

To obtain my master's degree, I am conducting a study in the field of web design as part of my master thesis. All submitted designs will therefore be used for study purposes. In order to achieve a homogeneous group, I would like to encourage not only male but also female web designers to submit a design. All submitted designs will be used anonymously for the study and therefore do not allow any conclusions to be drawn about your person. Since this is a contest, the winner will be chosen randomly from all serious submissions. I would be really happy if you would support me in my study. I think the results could be very informative and also useful for your further work (I won't go into more detail here as it could skew the results - but once the contest is over, feel free to contact me. Of course I will also provide you with my results as soon as my work is finished). Below you will find a usecase and a description of what the website should include:

The company Bikeshop Morvalt is planning to relaunch its own website and would like to present itself primarily as a competent and leading consultant in the field of cargo bikes. The design should appeal to a broad audience and embody an urban lifestyle. In any case, the website should include a landing page, a product overview page and a product details page, also make sure to design as gender neutral as possible. You only design the website. So don't worry about hardware or software limitations, just create the best bike store design you can.

1 page

• landing page, product overview page, product details page
• onlineshop

```html
<!DOCTYPE html>
<html lang="en">
<head>
<meta charset="utf-8">
<title>Bikeshop Morvalt</title>
<link rel="stylesheet" href="https://fonts.googleapis.com/css2?family=Montserrat:wght@400;500;600;700;800&display=swap">
<style>
:root{
  --red:#e3193d;
  --blue:#2536a3;
  --blue-deep:#21349a;
  --ink:#2c2c2c;
  --muted:#666;
  --grey-bg:#e4e4e4;
  --dark:#2d2d2d;
  --darker:#1f1f1f;
  --white:#fff;
  --orange:#f28a1c;
}
*{box-sizing:border-box;margin:0;padding:0}
html,body{width:1200px;height:4806px;overflow:hidden}
body{position:relative;background:var(--white);font-family:'Montserrat',sans-serif;color:var(--ink)}
.abs{position:absolute}
.brand{font-family:'Montserrat',sans-serif;font-weight:700;color:var(--red);letter-spacing:2px;white-space:nowrap;line-height:1}
.brand-line{display:block}
.brand-dot{display:inline-block;border-radius:50%;background:var(--red);vertical-align:middle;margin-left:10px}

/* header */
.header-brand{left:52px;top:22px;font-size:34px}
.header-brand .brand-sub{font-size:22px;letter-spacing:5px;margin-top:4px;padding-left:46px}
.main-nav{left:519px;top:38px;display:flex;gap:22px;font-size:21px;letter-spacing:1.5px;color:#444}
.main-nav a{color:inherit;text-decoration:none}
.main-nav .active{font-weight:600;color:#222;border-bottom:2px solid #999;padding-bottom:8px}
.region{left:1020px;top:38px;width:126px;height:28px;background:#e6e6e6;font-size:14px;display:flex;align-items:center;gap:6px;padding-left:8px;color:#444}
.flag{width:28px;height:16px;background:linear-gradient(var(--red) 0 33%,#fff 33% 66%,var(--red) 66%)}

/* hero */
.hero-title{right:130px;top:155px;font-size:35px;font-weight:700;color:var(--blue);letter-spacing:3px}
.hero-bike{left:135px;top:205px;width:680px;height:330px;border-radius:40px;background:radial-gradient(ellipse at 55% 50%,#c9d6c9 0%,#e8ece8 55%,#fff 80%)}
.spec-label{font-size:15px;color:#555;letter-spacing:1px;text-align:right;right:144px}
.spec-value{font-size:16px;font-weight:700;color:#222;letter-spacing:1px;text-align:right;right:144px}
.spec-rule{left:1064px;top:292px;width:1px;height:198px;background:#555}
.note{font-size:15px;color:#555;letter-spacing:1px}

/* expect */
.expect{left:0;top:600px;width:1200px;height:1042px;background:linear-gradient(#eef0fa 0%,#b9c1ea 18%,#6577cc 40%,#2d40a6 65%,var(--blue-deep) 100%)}
.wave{left:0;top:598px}
.section-title{font-size:34px;font-weight:700;color:var(--blue);letter-spacing:3px;text-align:center;width:1200px;left:0}
.expect-rule{left:476px;top:842px;width:310px;height:1px;background:#6a79c6}
.expect-intro{left:160px;top:878px;width:880px;text-align:center;font-size:15.5px;line-height:23px;color:#222;letter-spacing:.8px}
.feature{width:210px;text-align:center;color:var(--white)}
.feature-art{width:112px;height:112px;margin:0 auto;border-radius:22px}
.feature h3{font-size:25px;font-weight:700;letter-spacing:2px;margin-top:26px}
.feature p{font-size:12px;font-weight:600;line-height:23px;letter-spacing:.5px;margin-top:6px}
.dot{width:8px;height:8px;border-radius:50%;border:2px solid #e07096}
.feature-rule{left:466px;top:1280px;width:318px;height:1px;background:#7a88cf}

/* discover */
.discover{left:0;top:1642px;width:1200px;height:1385px;background:var(--grey-bg)}
.discover-rule{left:560px;top:1739px;width:80px;height:3px;background:var(--red)}
.side-photo{width:300px;height:524px}
.product-card{left:300px;width:600px;height:524px;background:var(--white);box-shadow:0 2px 6px rgba(0,0,0,.25)}
.product-photo{left:70px;width:460px;height:298px;top:17px}
.product-name{left:170px;font-size:22px;font-weight:700;color:var(--blue);letter-spacing:2.5px}
.spec-line{left:124px;width:2px;background:#555}
.spec-item{left:170px;font-size:18px;color:#555;letter-spacing:.5px;line-height:20px}
.spec-item small{display:block;font-size:9px;color:#999;line-height:11px}
.spec-node{left:116px;width:18px;height:2px;background:#555}
.spec-node::after{content:"";position:absolute;left:4px;top:-5px;width:10px;height:10px;border:2px solid #555;border-radius:50%;background:#fff;box-sizing:border-box}
.browse{left:0;top:2928px;width:1200px;text-align:center;font-size:34px;font-weight:700;color:var(--red);letter-spacing:3.5px}

/* blog */
.blog-title{left:0;top:3072px;width:1200px;text-align:center;font-size:34px;font-weight:700;letter-spacing:3.5px;color:#222}
.blog-title span{color:var(--red)}
.blog-filter{left:0;top:3130px;width:1200px;text-align:center;font-size:17px;font-weight:700;color:var(--blue);letter-spacing:2px}
.post{width:290px}
.post-photo{height:225px;position:relative}
.post-date{position:absolute;left:10px;top:10px;width:38px;height:38px;background:var(--orange);color:#fff;font-size:11px;text-align:center;line-height:14px;padding-top:5px}
.post h4{font-size:11.5px;font-weight:700;line-height:18px;letter-spacing:.8px;margin-top:22px;width:230px}
.post p{font-size:10.5px;line-height:14px;color:#666;margin-top:12px;letter-spacing:.3px}
.post a{display:block;margin-top:8px;font-size:10px;color:#3aa84a;text-decoration:none;letter-spacing:.5px}
.news-rule{left:127px;top:3626px;width:377px;height:1px;background:#999}
.news-title{left:127px;top:3655px;font-size:34px;font-weight:700;color:var(--red);letter-spacing:3px}
.field{height:43px;background:#fff;box-shadow:1px 2px 5px rgba(0,0,0,.3);font-size:21px;color:#aaa;padding:8px 18px;letter-spacing:1px}
.pill{background:#fff;border-radius:24px;box-shadow:1px 2px 5px rgba(0,0,0,.3);font-size:21px;font-weight:700;color:var(--red);text-align:center;letter-spacing:2px;line-height:43px}

/* contact */
.contact{left:0;top:3831px;width:1200px;height:597px;background:var(--dark)}
.contact-head{top:3878px;font-size:22px;color:#fff;letter-spacing:1.5px}
.map{left:34px;top:3956px;width:615px;height:349px;border:5px solid #1f35c2;background:linear-gradient(135deg,#e9ecef,#d7e2ea 50%,#efe6d8)}
.sep{left:715px;width:1px;height:40px;background:#777}
.dark-field{left:776px;width:301px;background:#fff;font-size:21px;color:#aaa;padding:6px 18px;letter-spacing:1px}

/* footer */
.footer{left:0;top:4428px;width:1200px;height:378px;background:var(--darker)}
.footer-brand{left:140px;top:4492px;font-size:44px}
.footer-brand .brand-sub{font-size:28px;letter-spacing:5px;margin-top:6px;padding-left:46px}
.social{width:26px;height:26px;border:2px solid #bbb;border-radius:50%}
.contact-line{left:765px;font-size:15.5px;color:#eee;letter-spacing:1px}
.copyright{left:0;top:4755px;width:1200px;text-align:center;font-size:15px;color:#eee;letter-spacing:1px}
</style>
</head>
<body>

<header class="site-header">
  <div class="brand header-brand abs"><span class="brand-line">Bikeshop</span><span class="brand-line brand-sub">Morvalt<span class="brand-dot" style="width:9px;height:9px"></span></span></div>
  <nav class="main-nav abs">
    <a class="active" href="#">Home</a><a href="#">About</a><a href="#">Discover</a><a href="#">Blog</a><a href="#">Contact</a>
  </nav>
  <div class="region abs"><span class="flag"></span>Austria ▾</div>
</header>

<section class="hero">
  <h1 class="hero-title abs">Great People Great Deals</h1>
  <div class="hero-bike abs" role="img" aria-label="Green cargo bike with rear rack and wide tyres, side view"></div>
  <div class="note abs" style="left:84px;top:224px">Adjustable Stand</div>
  <div class="abs" style="left:178px;top:246px;width:1px;height:44px;background:#555"></div>
  <div class="spec-label abs" style="top:290px">Max Gross Weight</div>
  <div class="spec-value abs" style="top:322px">400lb / 200kg</div>
  <div class="spec-label abs" style="top:365px">Rear Passenger</div>
  <div class="spec-value abs" style="top:397px">130lb / 60kg</div>
  <div class="spec-label abs" style="top:440px">Max Speed</div>
  <div class="spec-value abs" style="top:472px">56mph</div>
  <div class="spec-rule abs"></div>
  <div class="abs" style="left:512px;top:505px;width:150px;height:1px;background:#555"></div>
  <div class="abs" style="left:512px;top:505px;width:1px;height:22px;background:#555"></div>
  <div class="note abs" style="left:380px;top:527px;text-align:center;line-height:18px">Extra Thik Tyres<br>DURABLE</div>
</section>

<section class="expect-section">
  <div class="expect abs"></div>
  <svg class="wave abs" width="1200" height="160" viewBox="0 0 1200 160" aria-hidden="true">
    <path d="M0 0 H1200 V84 C1100 70 960 60 860 120 C790 160 700 150 620 110 C520 60 420 10 300 22 C200 32 120 70 0 80 Z" fill="#fff"/>
  </svg>
  <h2 class="section-title abs" style="top:786px">What Can You Expect From Us?</h2>
  <div class="expect-rule abs"></div>
  <p class="expect-intro abs">Lorem ipsum dolor sit amet, consectetur adipiscing elit, sed do eiusmod tempor incididunt ut labore et dolore magna aliqua. Quis ipsum suspendisse ultrices gravida. Risus commodo viverra maecenas accumsan lacus vel facilisis.</p>

  <div class="feature abs" style="left:135px;top:1008px"><div class="feature-art" role="img" aria-label="Puzzle pieces illustration" style="background:linear-gradient(135deg,#2f8be0,#f5c32c 50%,#e9384f)"></div><h3>Features</h3><p>Lorem ipsum dolor sit amet, consectetur adipiscing elit, sed do eiusmod tempor</p></div>
  <div class="feature abs" style="left:380px;top:1008px"><div class="feature-art" role="img" aria-label="Toolbox illustration" style="background:linear-gradient(160deg,#4b6ed6,#e4334f 45%,#d82843)"></div><h3>Accessories</h3><p>Lorem ipsum dolor sit amet, consectetur adipiscing elit, sed do eiusmod tempor</p></div>
  <div class="feature abs" style="left:617px;top:1008px"><div class="feature-art" role="img" aria-label="Speech bubbles with thumbs up illustration" style="background:linear-gradient(135deg,#f6d531,#7fd07a 55%,#3fa85a)"></div><h3>Reviews</h3><p>Lorem ipsum dolor sit amet, consectetur adipiscing elit, sed do eiusmod tempor</p></div>
  <div class="feature abs" style="left:854px;top:1008px"><div class="feature-art" role="img" aria-label="Price tag illustration" style="background:linear-gradient(135deg,#fbc43a,#f08a1d)"></div><h3>Prices</h3><p>Lorem ipsum dolor sit amet, consectetur adipiscing elit, sed do eiusmod tempor</p></div>

  <div class="dot abs" style="left:364px;top:1116px"></div>
  <div class="dot abs" style="left:599px;top:1116px"></div>
  <div class="dot abs" style="left:836px;top:1116px"></div>
  <div class="feature-rule abs"></div>

  <div class="feature abs" style="left:143px;top:1325px"><div class="feature-art" role="img" aria-label="Handshake illustration" style="background:linear-gradient(135deg,#f5c32c,#e9384f 60%,#3c5bc8)"></div><h3>Partners</h3><p>Lorem ipsum dolor sit amet, consectetur adipiscing elit, sed do eiusmod tempor</p></div>
  <div class="feature abs" style="left:380px;top:1325px"><div class="feature-art" role="img" aria-label="Parcel delivery illustration" style="background:linear-gradient(160deg,#6cc36c,#f2c9a3 45%,#e58c62)"></div><h3>Deliveries</h3><p>Lorem ipsum dolor sit amet, consectetur adipiscing elit, sed do eiusmod tempor</p></div>
  <div class="feature abs" style="left:617px;top:1325px"><div class="feature-art" role="img" aria-label="Flame with rising chart illustration" style="background:linear-gradient(160deg,#f7a531,#f26b1d 60%,#2f8be0)"></div><h3>Popularity</h3><p>Lorem ipsum dolor sit amet, consectetur adipiscing elit, sed do eiusmod tempor</p></div>
  <div class="feature abs" style="left:854px;top:1325px"><div class="feature-art" role="img" aria-label="Checklist with pencil illustration" style="background:radial-gradient(circle,#f2c33a 0 30%,#1f8a8a 31%,#15707a 100%);border-radius:50%"></div><h3>Advance Tech</h3><p>Lorem ipsum dolor sit amet, consectetur adipiscing elit, sed do eiusmod tempor</p></div>

  <div class="dot abs" style="left:364px;top:1433px"></div>
  <div class="dot abs" style="left:599px;top:1433px"></div>
  <div class="dot abs" style="left:836px;top:1433px"></div>
</section>

<section class="discover-section">
  <div class="discover abs"></div>
  <h2 class="section-title abs" style="top:1691px">DISCOVER</h2>
  <div class="discover-rule abs"></div>

  <div class="side-photo abs" style="left:0;top:1803px;background:linear-gradient(90deg,#e9e9e9,#d8d8d8)" role="img" aria-label="Faded photo of a front-loader cargo bike"></div>
  <div class="side-photo abs" style="left:900px;top:1803px;background:linear-gradient(90deg,#e6eaee,#dfe5ec)" role="img" aria-label="Faded photo of a light blue e-bike"></div>
  <article class="product-card abs" style="top:1803px">
    <div class="product-photo abs" role="img" aria-label="Orange longtail cargo bike with two child seats and front basket" style="background:radial-gradient(ellipse,#f4c08c 0%,#f1e6da 50%,#fff 75%)"></div>
    <div class="spec-line abs" style="top:352px;height:150px"></div>
    <div class="spec-node abs" style="top:352px"></div>
    <h3 class="product-name abs" style="top:338px">Adventure Max Pro 34x</h3>
    <div class="spec-node abs" style="top:394px"></div>
    <div class="spec-item abs" style="top:382px">Stylish And Comfort<small>Build with Compact Hardwares</small></div>
    <div class="spec-node abs" style="top:439px"></div>
    <div class="spec-item abs" style="top:427px">Durable Tyres<small>Perfect For Extra Grip</small></div>
    <div class="spec-node abs" style="top:484px"></div>
    <div class="spec-item abs" style="top:472px">Clever With Capability<small>Made For Both Home and Professional Use</small></div>
  </article>

  <div class="side-photo abs" style="left:0;top:2353px;background:linear-gradient(90deg,#f1ddc9,#e8d6c4)" role="img" aria-label="Faded photo of an orange e-bike"></div>
  <div class="side-photo abs" style="left:900px;top:2353px;background:linear-gradient(90deg,#eee6cf,#e6e0d0)" role="img" aria-label="Faded photo of a yellow cargo bike"></div>
  <article class="product-card abs" style="top:2353px">
    <div class="product-photo abs" role="img" aria-label="Black front-box cargo bike" style="background:radial-gradient(ellipse,#8d8d8d 0%,#dcdcdc 45%,#fff 75%)"></div>
    <div class="spec-line abs" style="top:352px;height:150px"></div>
    <div class="spec-node abs" style="top:352px"></div>
    <h3 class="product-name abs" style="top:338px">Monza Ride 98</h3>
    <div class="spec-node abs" style="top:394px"></div>
    <div class="spec-item abs" style="top:382px">Lots Of Space<small>Get Along With Stuff</small></div>
    <div class="spec-node abs" style="top:439px"></div>
    <div class="spec-item abs" style="top:427px">Comfy at Best<small>All The Grip</small></div>
    <div class="spec-node abs" style="top:484px"></div>
    <div class="spec-item abs" style="top:472px">Customizable<small>Set How You Want</small></div>
  </article>

  <div class="browse abs">Browse All Categories</div>
</section>

<section class="blog-section">
  <h2 class="blog-title abs">Top in Our <span>Blog</span></h2>
  <div class="blog-filter abs">All</div>

  <article class="post abs" style="left:127px;top:3197px">
    <div class="post-photo" role="img" aria-label="Close-up of a bike chainring" style="background:linear-gradient(135deg,#3a3330,#8a7d74 50%,#2b2522)"><span class="post-date">Sep<br>08</span></div>
    <h4>New Modifications Shared In Hyper League</h4>
    <p>Lorem ipsum dolor sit amet, consectetur adipiscing elit, sed do eiusmod tempor incididunt ore et dolore magna aliqua. Quis ipsum suspendisse ultrigravida. Risus commodo viver accumsan lacvel facilisis.</p>
    <a href="#">Read More</a>
  </article>
  <article class="post abs" style="left:455px;top:3197px">
    <div class="post-photo" role="img" aria-label="Road bike handlebar in dark studio light" style="background:linear-gradient(135deg,#5a5d60,#2a2c2e 55%,#6d7073)"><span class="post-date">Sep<br>07</span></div>
    <h4>All Pleasure Is Just A Ride Away</h4>
    <p>Lorem ipsum dolor sit amet, consectetur adipiscing elit, sed do eiusmod tempor incididunt ore et dolore magna aliqua. Quis ipsum suspen ultrgravida. Risumodo viver accumsan lacve.</p>
    <a href="#">Read More</a>
  </article>
  <article class="post abs" style="left:782px;top:3197px">
    <div class="post-photo" role="img" aria-label="Rear cassette and derailleur on a blue bike" style="background:linear-gradient(135deg,#1d3a73,#7d8a98 50%,#2a4b8a)"><span class="post-date">Sep<br>04</span></div>
    <h4>All The Gear Up, Giving A Worth</h4>
    <p>Lorem ipsum dolor sit amet, consectetur adipiscing elit, sed do eiusmod tempor incididunt ore et dolore magna aliqua. Quis ipsum suspendisse ultrigravida. Risus viver accumsan lacvel facilisis.</p>
    <a href="#">Read More</a>
  </article>

  <div class="news-rule abs"></div>
  <h2 class="news-title abs">Subscribe To Our Newsletter</h2>
  <div class="field abs" style="left:131px;top:3730px;width:300px">Name*</div>
  <div class="field abs" style="left:468px;top:3730px;width:301px">Email*</div>
  <div class="pill abs" style="left:797px;top:3730px;width:151px">SUBMIT</div>
</section>

<section class="contact-section">
  <div class="contact abs"></div>
  <h3 class="contact-head abs" style="left:34px;font-weight:500">Find Your Nearest Cargo Bike Dealer</h3>
  <h3 class="contact-head abs" style="left:776px;font-weight:500">We're Just a Text Away. Ask Us</h3>
  <div class="map abs" role="img" aria-label="Street map of the city centre with a dealer location pin"></div>
  <div class="sep abs" style="top:4020px"></div>
  <div class="sep abs" style="top:4125px"></div>
  <div class="sep abs" style="top:4215px"></div>
  <div class="dark-field abs" style="top:3960px;height:41px">Name*</div>
  <div class="dark-field abs" style="top:4027px;height:41px">Email*</div>
  <div class="dark-field abs" style="top:4092px;height:144px">Your Query</div>
  <div class="pill abs" style="left:776px;top:4260px;width:150px;line-height:45px">SEND</div>
</section>

<footer class="site-footer">
  <div class="footer abs"></div>
  <div class="brand footer-brand abs"><span class="brand-line">Bikeshop</span><span class="brand-line brand-sub">Morvalt<span class="brand-dot" style="width:11px;height:11px"></span></span></div>
  <div class="social abs" style="left:194px;top:4647px" aria-label="Photo sharing profile"></div>
  <div class="social abs" style="left:243px;top:4647px" aria-label="Short message profile"></div>
  <div class="social abs" style="left:293px;top:4647px" aria-label="Social network page"></div>
  <div class="social abs" style="left:342px;top:4647px" aria-label="Community profile"></div>

  <svg class="abs" style="left:692px;top:4510px" width="28" height="34" viewBox="0 0 28 34" aria-hidden="true"><rect x="3" y="1" width="22" height="32" fill="#fff"/><g fill="#1f1f1f"><rect x="8" y="6" width="4" height="4"/><rect x="16" y="6" width="4" height="4"/><rect x="8" y="14" width="4" height="4"/><rect x="16" y="14" width="4" height="4"/><rect x="11" y="24" width="6" height="9"/></g></svg>
  <div class="contact-line abs" style="top:4518px">Lindengasse 14, Innsbruck Austria</div>
  <svg class="abs" style="left:690px;top:4580px" width="34" height="26" viewBox="0 0 34 26" aria-hidden="true"><rect x="2" y="2" width="30" height="22" rx="3" fill="none" stroke="#fff" stroke-width="3"/><path d="M3 4 L17 15 L31 4" fill="none" stroke="#fff" stroke-width="3"/></svg>
  <div class="contact-line abs" style="top:4584px">hello@morvalt.example</div>
  <svg class="abs" style="left:690px;top:4643px" width="34" height="34" viewBox="0 0 24 24" aria-hidden="true"><path fill="#fff" d="M6.6 10.8a15.1 15.1 0 0 0 6.6 6.6l2.2-2.2a1 1 0 0 1 1-.25 11.4 11.4 0 0 0 3.6.57 1 1 0 0 1 1 1V20a1 1 0 0 1-1 1A17 17 0 0 1 3 4a1 1 0 0 1 1-1h3.5a1 1 0 0 1 1 1c0 1.25.2 2.45.57 3.57a1 1 0 0 1-.25 1z"/></svg>
  <div class="contact-line abs" style="top:4651px">+43 512 000 00</div>
  <div class="copyright abs">All Right Reserved 2022, Bikeshop Morvalt</div>
</footer>

</body>
</html>
```